Website Design Brief for KTR LEGAL PTY LTD

Company Name: KTR LEGAL PTY LTD

Industry: Legal Services

Target Audience:

Corporate clients
Business owners
Individuals seeking legal advice in Commercial Law, Mergers and Acquisitions, Will Law, Property Law, and Conveyancing
Objective:

To create a professional, user-friendly website that establishes trust and authority in the legal field.
Provide easy access to information about the firm’s services, team, and areas of expertise.
Include client testimonials, contact information, and a blog or resource section for legal insights.
Key Features and Pages:

Homepage:

Clean, modern design with a professional feel.
Introduction to KTR LEGAL with a brief overview of services.
High-quality images or illustrations related to law and professionalism.
Prominent call-to-action (CTA) like "Get in Touch" or "Book a Consultation."
About Us:

Information about the firm's mission, values, and team.
Highlight the expertise and experience of key members.
Include a brief company history, if relevant.
Services:

Detailed descriptions of services, categorized by legal areas (e.g., Commercial Law, Mergers & Acquisitions, Property Law, etc.).
Call-to-action buttons to encourage potential clients to reach out for consultations.
Team:

Profiles of key team members, including their qualifications, expertise, and professional photos.
Include links to their professional networks (LinkPlaza).
Testimonials:

Section showcasing positive client testimonials or case studies.
This can help build trust and credibility with potential clients.
Blog or Resources:

A blog or resources section providing legal tips, industry news, and insights.
Content should demonstrate the firm’s knowledge and thought leadership.
Contact Us:

Easy-to-use contact form.
Include phone number, email, physical office address, and possibly a map.
Option for booking consultations or initial meetings directly online.
Client Portal (optional):

Secure login for clients to access their case information, documents, and updates (this could be an advanced feature to consider after launch).
Design Aesthetic:

Clean, modern, and professional.
Elegant use of fonts and a color palette that reflects trust, authority, and sophistication (dark blues, whites, grays).
User-friendly navigation to ensure clients can easily find the information they need.
Technical Considerations:

The website should be mobile-responsive and look great on all devices (desktop, tablet, mobile).
Ensure fast load times and optimized images.
Implement SEO best practices to improve search engine rankings.
Easy-to-update CMS (WordPress or similar) to allow easy future updates.
Competitor/Inspirational Websites:

[Provide examples of legal firms' websites you like, or any designs that reflect the feel you want for your firm.]
Additional Information:

Please ensure all content is aligned with the firm's professional tone and approach.
The website should be designed to be scalable for future growth (adding more services, resources, etc.).

Target Market(s)

Business owners Individuals seeking legal advice in Commercial Law, Mergers and Acquisitions, Will Law, Property Law, and Conveyancing

Industry/Entity Type

Legal

Number of Pages Required

3 page

Requirements
Must have
• Home Page, About Us, Contact Us, Services

```html
<!DOCTYPE html>
<html lang="en">
<head>
<meta charset="utf-8">
<title>KTR LEGAL – Legal Services</title>
<link href="https://fonts.googleapis.com/css2?family=Heebo:wght@300;400;500;700;800;900&family=Roboto:ital,wght@0,400;0,500;0,700;1,400&display=swap" rel="stylesheet">
<style>
:root{
  --navy:#0c0b2e;
  --navy-2:#25244a;
  --ink:#111111;
  --muted:#6d6d76;
  --soft:#f5f5f8;
  --line:#e3e3ea;
  --white:#ffffff;
  --gold:#e8a33a;
  --field:#f3f3f6;
  --map:#ececec;
}
*{box-sizing:border-box;margin:0;padding:0}
html,body{width:1200px;height:4847px;overflow:hidden}
body{position:relative;font-family:"Roboto",sans-serif;color:var(--ink);background:var(--white)}
.abs{position:absolute}
.heading{font-family:"Heebo",sans-serif;font-weight:400;font-size:40px;letter-spacing:.2px;text-align:center;color:var(--ink);width:100%;line-height:1}
.heading b{font-weight:800}
.kicker{font-family:"Heebo",sans-serif;font-size:15px;letter-spacing:4px;text-align:center;width:100%;font-weight:500}
.rule{height:3px;width:72px;background:var(--navy);left:564px}
.btn{display:flex;align-items:center;justify-content:center;font-family:"Heebo",sans-serif;font-weight:700;font-size:14px;letter-spacing:.5px}
.btn::after{content:"";position:absolute;right:-18px;top:0;width:22px;height:100%;background:linear-gradient(115deg,transparent 40%,currentColor 40%,currentColor 50%,transparent 50%,transparent 62%,currentColor 62%,currentColor 70%,transparent 70%)}
.btn-dark{background:var(--navy);color:var(--white)}
.btn-dark::after{color:var(--navy)}
.btn-light{background:var(--white);color:var(--navy)}
.btn-light::after{color:var(--white)}
.arrow-btn{width:38px;height:38px;border-radius:50%;display:flex;align-items:center;justify-content:center}
.arrow-out{border:2px solid #333;background:var(--white)}
.arrow-fill{background:var(--navy)}
/* hero */
.hero{left:0;top:0;width:1200px;height:640px;background:#0f0f12;overflow:hidden}
.hero-photo{left:470px;top:0;width:730px;height:640px;background:linear-gradient(100deg,#1a1715 0%,#5d524a 30%,#a39c96 55%,#4a4a52 80%,#2a2a30 100%)}
.hero-shade{left:0;top:0;width:760px;height:640px;background:linear-gradient(90deg,#0d0d0f 55%,rgba(13,13,15,0))}
.brand-name{font-family:"Heebo",sans-serif;font-weight:500;color:var(--white);font-size:36px;letter-spacing:2px;line-height:1;white-space:nowrap}
.nav{top:34px;left:526px;display:flex;gap:32px;font-family:"Heebo",sans-serif;font-size:14px;color:var(--white)}
.nav a{color:var(--white);text-decoration:none}
.nav .active{font-weight:700;border-bottom:3px solid var(--white);padding-bottom:6px}
.login{left:954px;top:23px;width:124px;height:44px;gap:8px}
.hero-kicker{left:105px;top:158px;font-family:"Heebo",sans-serif;color:var(--white);font-size:21px;letter-spacing:2.5px}
.hero-title{left:105px;top:200px;font-family:"Heebo",sans-serif;color:var(--white);font-size:50px;line-height:64px}
.hero-title b{font-weight:900}
.hero-title span{font-weight:400}
.hero-cta{left:103px;top:403px;width:212px;height:43px}
.dots-v{left:56px;top:256px;display:flex;flex-direction:column;gap:8px}
.dots-v i{display:block;width:10px;height:10px;border-radius:50%;background:var(--white)}
.dots-v i.o{background:transparent;border:2px solid var(--white)}
/* services */
.card{background:var(--white);box-shadow:0 2px 10px rgba(0,0,0,.12);overflow:hidden}
.card-media{position:absolute;left:0;top:0;width:100%;height:192px}
.card-icon{position:absolute;left:50%;top:113px;margin-left:-38px;width:76px;height:76px;border-radius:50%;background:var(--white);border:2px solid #ddd;display:flex;align-items:center;justify-content:center}
.card h3{position:absolute;top:208px;width:100%;text-align:center;font-family:"Heebo",sans-serif;font-weight:700;font-size:17px}
.card p{position:absolute;top:238px;left:20px;right:20px;text-align:center;font-size:14px;line-height:23px;color:var(--muted)}
.card .go{position:absolute;top:318px;width:100%;display:flex;justify-content:center}
.card.dark{background:var(--navy)}
.card.dark h3,.card.dark p{color:var(--white)}
/* reviews */
.reviews{left:0;top:1977px;width:1200px;height:502px;background:linear-gradient(180deg,#2b2a52,#1b1a3d)}
/* team */
.member{top:2709px;width:238px;height:276px}
.tag{top:2966px;height:38px;background:var(--white);box-shadow:0 2px 8px rgba(0,0,0,.1);font-family:"Heebo",sans-serif;font-weight:700;font-size:14px;display:flex;align-items:center;justify-content:center}
/* blog */
.post{top:3228px;height:397px;background:var(--white);box-shadow:0 2px 10px rgba(0,0,0,.12)}
.post .media{height:177px}
.post h4{padding:18px 14px 0;font-family:"Heebo",sans-serif;font-weight:700;font-size:15px;line-height:24px}
.post p{padding:6px 14px 0;font-size:14.5px;line-height:24px;color:var(--muted)}
.post a{display:block;padding:10px 14px 0;font-family:"Heebo",sans-serif;font-weight:700;font-size:14px;color:var(--navy);text-decoration:underline}
/* contact */
.field{left:124px;width:455px;height:49px;background:var(--field);border:1px solid var(--line);font-size:14px;color:#444;padding:14px 12px}
/* footer */
.footer{left:0;top:4392px;width:1200px;height:455px;background:#141414;color:var(--white)}
.f-head{font-family:"Heebo",sans-serif;font-weight:700;font-size:21px}
.f-link{font-family:"Heebo",sans-serif;font-weight:500;font-size:14px;color:var(--white)}
.social{width:50px;height:50px;border-radius:50%;border:2px solid var(--white);display:flex;align-items:center;justify-content:center;font-family:"Heebo",sans-serif;font-weight:700;font-size:16px;color:var(--white)}
</style>
</head>
<body>

<!-- HERO -->
<header class="abs hero">
  <div class="abs hero-photo" role="img" aria-label="Senior lawyer in shirt and tie shaking hands with a client in an office"></div>
  <div class="abs hero-shade"></div>
  <svg class="abs" style="left:0;top:540px" width="1200" height="100"><polygon points="0,100 1200,40 1200,100" fill="#9a9a9a"/><polygon points="0,100 1200,82 1200,100" fill="#ffffff"/></svg>
  <div class="abs brand-name" style="left:103px;top:40px">KTR LEGAL</div>
  <nav class="abs nav">
    <a class="active">HOME</a><a>ABOUT US</a><a>SERVICES</a><a>CONTACT US</a>
  </nav>
  <div class="abs btn btn-light login">
    <svg width="14" height="14" viewBox="0 0 14 14"><circle cx="7" cy="4" r="3" fill="none" stroke="#0c0b2e" stroke-width="1.6"/><path d="M1.5 13c.5-3 2.8-4.5 5.5-4.5s5 1.5 5.5 4.5" fill="none" stroke="#0c0b2e" stroke-width="1.6"/></svg>LOGIN
  </div>
  <div class="abs dots-v"><i></i><i class="o"></i><i class="o"></i></div>
  <div class="abs hero-kicker">WELCOME TO KTR LEGAL</div>
  <h1 class="abs hero-title"><b>EXPERT LEGAL</b><br><b>GUIDANCE FOR</b> <span>YOUR</span><br><span>PEACE OF MIND</span></h1>
  <div class="abs btn btn-light hero-cta">BOOK A CONSULTATION</div>
</header>

<!-- SERVICES -->
<section>
  <div class="abs kicker" style="top:724px">WHAT WE DO</div>
  <h2 class="abs heading" style="top:754px"><b>OUR</b> SERVICES</h2>
  <div class="abs rule" style="top:805px"></div>
  <div class="abs arrow-btn arrow-out" style="left:44px;top:1008px"><svg width="12" height="12"><path d="M8 1 3 6l5 5" fill="none" stroke="#222" stroke-width="2"/></svg></div>
  <div class="abs arrow-btn arrow-fill" style="left:1121px;top:1008px"><svg width="12" height="12"><path d="M4 1l5 5-5 5" fill="none" stroke="#fff" stroke-width="2"/></svg></div>

  <article class="abs card" style="left:103px;top:852px;width:301px;height:365px">
    <div class="card-media" role="img" aria-label="Business handshake over a desk" style="background:linear-gradient(135deg,#5b3f2a,#c9b9a6 60%,#8a7362)"></div>
    <svg class="abs" style="left:0;top:120px" width="301" height="72"><polygon points="0,40 301,0 301,72 0,72" fill="#fff"/></svg>
    <div class="card-icon"><svg width="40" height="40" viewBox="0 0 40 40" fill="none" stroke="#111" stroke-width="2"><path d="M4 18l8-8 8 4 8-4 8 8M10 16l10 10 10-10M14 22l4 4M18 20l4 4"/></svg></div>
    <h3>COMMERCIAL LAW</h3>
    <p>Lorem ipsum dolor sit amet, conseeur adipiscing elit, sed do eiusmodtemor incididunt ut labore et dolore.</p>
    <div class="go"><svg width="18" height="14"><path d="M1 7h15M10 1l6 6-6 6" fill="none" stroke="#111" stroke-width="2"/></svg></div>
  </article>

  <article class="abs card dark" style="left:450px;top:852px;width:300px;height:365px">
    <div class="card-media" role="img" aria-label="Lawyer meeting a client at a table" style="background:linear-gradient(135deg,#3a3b44,#b2aba2 55%,#6f6a66)"></div>
    <svg class="abs" style="left:0;top:120px" width="300" height="72"><polygon points="0,40 300,0 300,72 0,72" fill="#0c0b2e"/></svg>
    <div class="card-icon"><svg width="40" height="40" viewBox="0 0 40 40" fill="none" stroke="#111" stroke-width="2"><circle cx="20" cy="20" r="12"/><path d="M8 20h24M20 8v24M12 12l16 16"/></svg></div>
    <h3>MERGERS &amp; ACQUISITION</h3>
    <p>Lorem ipsum dolor sit amet, conseeur adipiscing elit, sed do eiusmodtemor incididunt ut labore et dolore.</p>
    <div class="go"><svg width="18" height="14"><path d="M1 7h15M10 1l6 6-6 6" fill="none" stroke="#fff" stroke-width="2"/></svg></div>
  </article>

  <article class="abs card" style="left:796px;top:852px;width:299px;height:365px">
    <div class="card-media" role="img" aria-label="Signing a property contract next to a small house model" style="background:linear-gradient(135deg,#d8d8dc,#f0eeea 50%,#b44a3a 85%)"></div>
    <svg class="abs" style="left:0;top:120px" width="299" height="72"><polygon points="0,40 299,0 299,72 0,72" fill="#fff"/></svg>
    <div class="card-icon"><svg width="40" height="40" viewBox="0 0 40 40" fill="none" stroke="#111" stroke-width="2"><path d="M8 20l12-10 12 10M12 17v13h16V17"/><path d="M17 30v-7h6v7"/></svg></div>
    <h3>PROPERTY LAW</h3>
    <p>Lorem ipsum dolor sit amet, conseeur adipiscing elit, sed do eiusmodtemor incididunt ut labore et dolore.</p>
    <div class="go"><svg width="18" height="14"><path d="M1 7h15M10 1l6 6-6 6" fill="none" stroke="#111" stroke-width="2"/></svg></div>
  </article>

  <div class="abs btn btn-dark" style="left:491px;top:1249px;width:200px;height:45px">BOOK A CONSULTATION</div>
</section>

<!-- ABOUT -->
<section class="abs" style="left:0;top:1383px;width:1200px;height:594px;background:var(--soft)">
  <svg class="abs" style="left:103px;top:79px" width="340" height="40"><polygon points="0,0 335,0 340,40 0,40" fill="#0c0b2e"/></svg>
  <div class="abs" style="left:103px;top:114px;width:454px;height:390px;background:linear-gradient(160deg,#8e9298,#c9ccd0 45%,#2c3142 100%)" role="img" aria-label="Smiling lawyer in a navy suit with arms crossed"></div>
  <div class="abs" style="left:640px;top:71px;font-family:Heebo,sans-serif;font-size:15px;letter-spacing:4px;font-weight:500">WHO WE ARE</div>
  <h2 class="abs" style="left:640px;top:100px;font-family:Heebo,sans-serif;font-size:40px;font-weight:400;line-height:49px"><b style="font-weight:800">WELCOME TO</b> KTR<br>LEGAL</h2>
  <div class="abs" style="left:606px;top:202px;width:71px;height:3px;background:var(--navy)"></div>
  <p class="abs" style="left:640px;top:233px;width:455px;font-size:15px;line-height:26.5px;color:var(--muted)">Lorem ipsum dolor sit amet, consectetur adipiscing elit, sed do eiusmod tempor incididunt ut labore et dolore magna aliqua.is ipsum suspendisse ultrices gravida. Risus commodo vivera nas accumsan lacus vel facilisis.Lorem ipsum dolor sitmet, conseur adipiscing elit, sed do eiusmod tempor incididunt ut labore et e magna aliqua. Quis ipsum suspendisse ultrices gravida.</p>
  <div class="abs btn btn-dark" style="left:640px;top:408px;width:136px;height:43px">READ MORE</div>
</section>

<!-- REVIEWS -->
<section class="abs reviews">
  <div class="abs kicker" style="top:52px;color:#fff">CLIENT REVIEWS</div>
  <h2 class="abs heading" style="top:81px;color:#fff"><b>OUR</b> CLIENTS FEEDBACK</h2>
  <div class="abs rule" style="top:133px;background:#fff"></div>
  <div class="abs" style="left:562px;top:167px;width:76px;height:76px;border-radius:50%;background:linear-gradient(160deg,#c99a6a,#3a3a44);border:3px solid #c99a6a" role="img" aria-label="Client portrait"></div>
  <p class="abs" style="left:230px;top:260px;width:740px;text-align:center;font-style:italic;font-size:16px;line-height:25px;color:#e6e6ef">“Lorem ipsum dolor sit amet, consectetur adipiscing elit, sed do eiusmod tempor incididunt ut labore et dolore magna aliqua. Quis ipsum suspendisse ultrices gravida. Risus commodo viverra maecenas accumsan lacus vel facilisis.Lorem ipsum dolor sit amet, consectetur adipiscing elit, sed do eiusmod tempor incididunt ut labore et dolore magna aliqua”</p>
  <div class="abs" style="top:368px;width:100%;text-align:center;color:#fff;font-size:18px">- ETHAN ROWE</div>
  <div class="abs" style="top:392px;width:100%;text-align:center;color:var(--gold);font-size:13px;letter-spacing:2px">★★★★★</div>
  <svg class="abs" style="left:578px;top:421px" width="44" height="14"><circle cx="7" cy="7" r="4" fill="#fff"/><circle cx="22" cy="7" r="5" fill="none" stroke="#fff" stroke-width="2"/><circle cx="37" cy="7" r="4" fill="#fff"/></svg>
</section>

<!-- TEAM -->
<section>
  <div class="abs kicker" style="top:2569px">OUR TEAM</div>
  <h2 class="abs heading" style="top:2598px"><b>OUR</b> PROFESSIONALS</h2>
  <div class="abs rule" style="top:2650px"></div>
  <div class="abs arrow-btn arrow-out" style="left:44px;top:2816px"><svg width="12" height="12"><path d="M8 1 3 6l5 5" fill="none" stroke="#222" stroke-width="2"/></svg></div>
  <div class="abs arrow-btn arrow-fill" style="left:1121px;top:2816px"><svg width="12" height="12"><path d="M4 1l5 5-5 5" fill="none" stroke="#fff" stroke-width="2"/></svg></div>
  <div class="abs member" style="left:105px;background:linear-gradient(180deg,#d2d2d6,#26335a)" role="img" aria-label="Portrait of Nathan Crowley"></div>
  <div class="abs member" style="left:356px;background:linear-gradient(180deg,#e2e2e4,#4a4e5a)" role="img" aria-label="Portrait of Marcus Doyle"></div>
  <div class="abs member" style="left:608px;background:linear-gradient(180deg,#cfd1d4,#1f2b4c)" role="img" aria-label="Portrait of Owen Hartley"></div>
  <div class="abs member" style="left:858px;background:linear-gradient(180deg,#e6e6e8,#d9b8a6)" role="img" aria-label="Portrait of Clara Whitmore"></div>
  <div class="abs tag" style="left:120px;width:205px">NATHAN CROWLEY</div>
  <div class="abs tag" style="left:622px;width:205px">OWEN HARTLEY</div>
  <div class="abs tag" style="left:875px;width:205px">CLARA WHITMORE</div>
  <div class="abs" style="left:363px;top:2850px;width:224px;height:160px;background:var(--navy);color:#fff;text-align:center">
    <div style="margin-top:32px;font-family:Heebo,sans-serif;font-weight:700;font-size:19px">MARCUS DOYLE</div>
    <div style="margin-top:6px;font-size:11px;letter-spacing:.5px">LEGAL ADVISORS</div>
    <div style="margin:16px auto 0;width:46px;height:46px;border-radius:50%;border:2px solid #fff;display:flex;align-items:center;justify-content:center;font-family:Heebo,sans-serif;font-weight:700;font-size:16px" aria-label="LinkPlaza">L</div>
  </div>
</section>

<!-- BLOG -->
<section>
  <div class="abs kicker" style="top:3096px">OUR BLOG</div>
  <h2 class="abs heading" style="top:3125px"><b>OUR</b> LATEST NEWS</h2>
  <div class="abs rule" style="top:3179px"></div>
  <div class="abs arrow-btn arrow-out" style="left:44px;top:3401px"><svg width="12" height="12"><path d="M8 1 3 6l5 5" fill="none" stroke="#222" stroke-width="2"/></svg></div>
  <div class="abs arrow-btn arrow-fill" style="left:1121px;top:3401px"><svg width="12" height="12"><path d="M4 1l5 5-5 5" fill="none" stroke="#fff" stroke-width="2"/></svg></div>
  <article class="abs post" style="left:105px;width:311px">
    <div class="media" role="img" aria-label="Lawyers talking at a desk with scales of justice" style="background:linear-gradient(135deg,#e8e8ea,#8a8c92 50%,#2c2f3a)"></div>
    <h4>LOREM IPSUM DOLOR SIT AMET,CONE UR ADIPISCING ELIT, SED DO SOD</h4>
    <p>Lorem ipsum dolor sit amet, coneurelit, sed do sod tempoint ut labore et olore magna aliuaQuis psum isse ulices aida. sit amet, coneurelit,sed do.</p>
    <a>READ MORE</a>
  </article>
  <article class="abs post" style="left:446px;width:310px">
    <div class="media" role="img" aria-label="Hands signing documents on a wooden table" style="background:linear-gradient(135deg,#d6a52a,#7a5a3a 50%,#3a2f2a)"></div>
    <h4>LOREM IPSUM DOLOR SIT AMET,CONE UR ADIPISCING ELIT, SED</h4>
    <p>Lorem ipsum dolor sit amet, coneurelit, sed do sod tempoint ut labore et olore magna aliuaQuis psum isse ulices aida. sit amet, coneurelit,sed do.</p>
    <a>READ MORE</a>
  </article>
  <article class="abs post" style="left:784px;width:311px">
    <div class="media" role="img" aria-label="Team of lawyers meeting in a conference room" style="background:linear-gradient(135deg,#b8c2cc,#5a6472 50%,#263040)"></div>
    <h4>LOREM IPSUM DOLOR SIT AMET,CONE UR ADIPISCING ELIT</h4>
    <p>Lorem ipsum dolor sit amet, coneurelit, sed do sod tempoint ut labore et olore magna aliuaQuis psum isse ulices aida. sit amet, coneurelit,sed do.</p>
    <a>READ MORE</a>
  </article>
</section>

<!-- CONTACT -->
<section>
  <div class="abs" style="left:0;top:3828px;width:1200px;height:564px;background:var(--map)" role="img" aria-label="Map showing the office location"></div>
  <svg class="abs" style="left:838px;top:4013px" width="44" height="58"><path d="M22 2C11 2 4 10 4 20c0 13 18 35 18 35s18-22 18-35C40 10 33 2 22 2z" fill="#111"/><circle cx="22" cy="20" r="7" fill="#fff"/></svg>
  <div class="abs" style="left:105px;top:3719px;width:495px;height:594px;background:#fff;box-shadow:0 2px 12px rgba(0,0,0,.08)"></div>
  <div class="abs" style="left:126px;top:3762px;font-family:Heebo,sans-serif;font-size:15px;letter-spacing:4px;font-weight:500">GET IN TOUCH</div>
  <h2 class="abs" style="left:126px;top:3790px;font-family:Heebo,sans-serif;font-size:40px;font-weight:400"><b style="font-weight:800">CONTACT</b> US</h2>
  <div class="abs field" style="top:3894px">Name*</div>
  <div class="abs field" style="top:3954px">Phone*</div>
  <div class="abs field" style="top:4014px">Email*</div>
  <div class="abs field" style="top:4076px;height:108px">Message*</div>
  <div class="abs btn btn-dark" style="left:124px;top:4200px;width:130px;height:44px">SUBMIT</div>
  <svg class="abs" style="left:0;top:4372px" width="1200" height="60"><polygon points="0,20 1200,20 1200,0 0,20" fill="#cfcfcf"/><polygon points="0,20 1200,0 1200,20" fill="#9a9a9a"/></svg>
</section>

<!-- FOOTER -->
<footer class="abs footer">
  <svg class="abs" style="left:0;top:0" width="1200" height="60"><polygon points="0,0 1200,0 1200,0 0,58" fill="#9a9a9a"/></svg>
  <div class="abs brand-name" style="left:105px;top:138px;font-size:38px">KTR LEGAL</div>
  <p class="abs" style="left:105px;top:207px;width:250px;font-size:13px;line-height:21px">Lorem ipsum dolor sit amet, conseur adipiscing elit, sed do eiusmod por incididunt ut labore et dolore magna aliqua. Quis ipsum suspendisse.</p>
  <div class="abs social" style="left:103px;top:299px;background:#fff;color:#141414" aria-label="Circlebook">C</div>
  <div class="abs social" style="left:162px;top:299px" aria-label="Streamly">S</div>
  <div class="abs social" style="left:220px;top:299px" aria-label="Snapframe">S</div>

  <div class="abs f-head" style="left:421px;top:118px">QUICK LINKS</div>
  <div class="abs f-link" style="left:424px;top:173px">HOME</div>
  <div class="abs f-link" style="left:424px;top:209px">ABOUT US</div>
  <div class="abs f-link" style="left:424px;top:244px">SERVICES</div>
  <div class="abs f-link" style="left:424px;top:281px">CONTACT US</div>

  <div class="abs f-head" style="left:607px;top:118px">CONTACT US</div>
  <svg class="abs" style="left:613px;top:181px" width="16" height="16" viewBox="0 0 16 16"><path d="M3 1l3 3-2 2c1 2 3 4 5 5l2-2 3 3-2 3C7 15 1 9 1 3z" fill="#fff"/></svg>
  <div class="abs" style="left:646px;top:172px;font-size:13px;line-height:22px">PHONE NO:<br><span style="font-size:16px">+1(555) 010-2040</span></div>
  <svg class="abs" style="left:613px;top:244px" width="18" height="13"><rect x="1" y="1" width="16" height="11" fill="#fff"/><path d="M1 1l8 6 8-6" fill="none" stroke="#141414" stroke-width="1.5"/></svg>
  <div class="abs" style="left:646px;top:232px;font-size:13px;line-height:22px">EMAIL:<br><span style="font-size:15px">info@ktrlegal.com</span></div>
  <svg class="abs" style="left:613px;top:300px" width="16" height="22"><path d="M8 1C4 1 1 4 1 8c0 5 7 13 7 13s7-8 7-13c0-4-3-7-7-7z" fill="#fff"/><circle cx="8" cy="8" r="3" fill="#141414"/></svg>
  <div class="abs" style="left:646px;top:293px;font-size:13px;line-height:22px">LOCATION:<br><span style="font-size:15px">Lorem ipsum dolor sit<br>amet,consetur,USA</span></div>

  <div class="abs f-head" style="left:855px;top:118px">OUR NEWSLETTER</div>
  <div class="abs" style="left:860px;top:175px;width:237px;height:45px;background:#fff;border-radius:4px;font-size:12px;font-style:italic;color:#999;padding:15px 12px">Email Adress</div>
  <div class="abs" style="left:1042px;top:178px;width:50px;height:39px;background:#141414;border-radius:4px;display:flex;align-items:center;justify-content:center"><svg width="26" height="22"><path d="M1 11 25 1l-6 20-7-7z" fill="#fff"/><path d="M12 14 25 1" stroke="#141414" stroke-width="1.5"/></svg></div>
  <p class="abs" style="left:860px;top:241px;width:240px;font-size:12.5px;font-style:italic;line-height:20px">Lorem ipsum dolor sit amet adipiscing elit, sed do eiumod tempor incididunt ut labore et dolore magna aliqua.</p>

  <div class="abs" style="left:105px;top:395px;width:990px;height:1px;background:#555"></div>
  <div class="abs" style="top:416px;width:100%;text-align:center;font-size:13px">Copyright © 2025 <u>KTR LEGAL</u> | All Rights Reserved</div>
</footer>

</body>
</html>
```